Business Card and Stationary for a Trucking Company
Silver Brook Haulage, INC.
Business Card and Stationary for a Trucking Company - Transportation
Creative Brief
Professional
Teodoro Maravel
President
318 North Pellham Avenue Suite 2270 Los Angeles, CA 90017
tmaravel7@brookmail.example
www.silverbrookhaulage.example

```html
<!DOCTYPE html>
<html lang="en">
<head>
<meta charset="utf-8">
<title>Silver Brook Haulage, INC. — Business Card</title>
<link href="https://fonts.googleapis.com/css2?family=Source+Sans+3:wght@400;600;700&display=swap" rel="stylesheet">
<style>
  :root {
    --backdrop: #e6e8eb;
    --card: #fbfbfb;
    --brand-blue: #2379b4;
    --deep-blue: #1b5f93;
    --gold: #d2b77a;
    --ink: #2a4a66;
    --muted: #6b7682;
    --divider: #c9ced4;
  }
  * { box-sizing: border-box; margin: 0; padding: 0; }
  html, body {
    width: 1200px; height: 901px; overflow: hidden;
    background: var(--backdrop);
    font-family: "Source Sans 3", "Helvetica Neue", Arial, sans-serif;
  }
  .canvas {
    width: 1200px; height: 901px;
    display: flex; flex-direction: column; align-items: center; justify-content: center;
    gap: 56px;
  }
  .card {
    position: relative;
    width: 620px; height: 354px;
    background: var(--card);
    border-radius: 16px;
    overflow: hidden;
    box-shadow: 0 6px 22px rgba(30, 45, 60, 0.18);
  }

  /* back side */
  .card-back .brand-mark {
    position: absolute; left: 0; right: 0; top: 118px;
    display: flex; align-items: center; justify-content: center; gap: 16px;
  }
  .brand-dot {
    width: 40px; height: 40px; border-radius: 50%;
    background: var(--brand-blue);
  }
  .card-back .brand-name {
    font-weight: 700; font-size: 34px; color: var(--brand-blue); letter-spacing: 0.3px;
  }
  .card-back .web {
    position: absolute; left: 54px; bottom: 40px;
    font-size: 14px; letter-spacing: 4px; color: var(--muted);
  }

  /* front side */
  .card-front .brand-name {
    position: absolute; left: 40px; top: 108px; width: 260px;
    font-weight: 700; font-size: 27px; line-height: 1.1; color: var(--brand-blue);
  }
  .card-front .divider {
    position: absolute; left: 330px; top: 50px; width: 1px; height: 150px;
    background: var(--divider);
  }
  .contact {
    position: absolute; left: 352px; top: 58px; color: var(--ink);
  }
  .contact .person { font-weight: 700; font-size: 20px; color: var(--deep-blue); }
  .contact .role { font-size: 13px; color: var(--muted); margin-bottom: 14px; }
  .contact .address { font-size: 13.5px; line-height: 1.3; margin-bottom: 6px; }
  .contact .line { display: flex; align-items: center; gap: 7px; font-size: 13.5px; line-height: 1.35; }
  .contact svg { width: 13px; height: 13px; fill: var(--deep-blue); flex: none; }
  .wave { position: absolute; left: 0; bottom: 0; width: 620px; height: 140px; }
  .card-front .web {
    position: absolute; left: 44px; bottom: 20px;
    font-size: 14px; letter-spacing: 4px; color: #ffffff;
  }
</style>
</head>
<body>
<main class="canvas">

  <section class="card card-back" aria-label="Card back">
    <div class="brand-mark">
      <span class="brand-dot"></span>
      <span class="brand-name">Silver Brook Haulage, INC.</span>
    </div>
    <p class="web">www.silverbrookhaulage.example</p>
  </section>

  <section class="card card-front" aria-label="Card front">
    <p class="brand-name">Silver Brook Haulage, INC.</p>
    <span class="divider"></span>
    <div class="contact">
      <p class="person">Teodoro Maravel</p>
      <p class="role">President</p>
      <p class="address">318 North Pellham Avenue<br>Suite 2270<br>Los Angeles, CA 90017</p>
      <p class="line">
        <svg viewBox="0 0 24 24"><path d="M6.6 10.8a15 15 0 0 0 6.6 6.6l2.2-2.2a1 1 0 0 1 1-.25 11.4 11.4 0 0 0 3.6.57 1 1 0 0 1 1 1V20a1 1 0 0 1-1 1A17 17 0 0 1 3 4a1 1 0 0 1 1-1h3.5a1 1 0 0 1 1 1c0 1.25.2 2.45.57 3.57a1 1 0 0 1-.25 1z"/></svg>
        (213) 555-0148
      </p>
      <p class="line">
        <svg viewBox="0 0 24 24"><path d="M2 5h20v14H2z M2 5l10 8 10-8" fill="none" stroke="#1b5f93" stroke-width="2"/></svg>
        tmaravel7@brookmail.example
      </p>
    </div>
    <svg class="wave" viewBox="0 0 620 140" preserveAspectRatio="none" aria-hidden="true">
      <path d="M0 70 C 180 20, 420 20, 620 60 L620 140 L0 140 Z" fill="var(--gold)"/>
      <path d="M0 82 C 180 34, 420 34, 620 72 L620 140 L0 140 Z" fill="var(--card)"/>
      <path d="M0 92 C 190 46, 420 46, 620 84 L620 140 L0 140 Z" fill="var(--brand-blue)"/>
    </svg>
    <p class="web">www.silverbrookhaulage.example</p>
  </section>

</main>
</body>
</html>
```